Business card for my company-RKV Design Studio

I do not have a logo-I like red and keeping it clean. Information that should be on the card:
Tom Brazenhall AIA
Architecture Planning Interiors
Cell Phone-614.529.4086
email-rkvplanner4@mailvane.net
www.rkvdesignstudio.net

```html
<!DOCTYPE html>
<html lang="en">
<head>
<meta charset="utf-8">
<title>RKV Design Studio – Business Card</title>
<link rel="stylesheet" href="https://fonts.googleapis.com/css2?family=Bodoni+Moda:wght@400;500&family=Montserrat:ital,wght@0,300;0,700;1,300&display=swap">
<style>
  :root {
    --stage: #c9c9c9;
    --card: #ffffff;
    --red: #ff0000;
    --ink: #2b2b2b;
    --muted: #555555;
    --night: #050208;
    --border: #1a1a1a;
  }
  * { box-sizing: border-box; margin: 0; padding: 0; }
  html, body {
    width: 1200px;
    height: 846px;
    overflow: hidden;
    background: var(--stage);
  }
  .card {
    position: absolute;
    left: 346px;
    width: 509px;
    height: 291px;
  }
  /* Front */
  .card-front {
    top: 114px;
    background: var(--card);
    border: 1px solid var(--border);
  }
  .accent-band {
    position: absolute;
    left: 0; top: 0; bottom: 0;
    width: 23px;
    background: var(--red);
  }
  .studio-name {
    position: absolute;
    left: 85px;
    top: 44px;
    font-family: "Bodoni Moda", serif;
    font-weight: 400;
    font-size: 31px;
    line-height: 1;
    color: var(--ink);
  }
  .person-name {
    position: absolute;
    left: 85px;
    top: 110px;
    font-family: "Montserrat", sans-serif;
    font-weight: 700;
    font-size: 18px;
    line-height: 1;
    color: var(--red);
  }
  .person-role {
    position: absolute;
    left: 85px;
    top: 132px;
    font-family: "Montserrat", sans-serif;
    font-style: italic;
    font-weight: 300;
    font-size: 11.5px;
    line-height: 1;
    color: var(--muted);
  }
  .contact-line {
    position: absolute;
    left: 85px;
    display: flex;
    align-items: center;
    gap: 6px;
    font-family: "Montserrat", sans-serif;
    font-weight: 300;
    font-size: 14.5px;
    line-height: 1;
    color: var(--ink);
    white-space: nowrap;
  }
  .contact-line svg {
    width: 18px;
    height: 18px;
    flex: none;
    stroke: var(--ink);
    stroke-width: 1;
    fill: none;
  }
  .contact-phone { top: 163px; }
  .contact-email { top: 186px; }
  .contact-web { top: 208px; }
  .contact-address { top: 241px; }
  .contact-address svg { height: 24px; }

  /* Back */
  .card-back {
    top: 442px;
    background: var(--night);
    overflow: hidden;
  }
  .building-photo {
    position: absolute;
    inset: 0;
    background: linear-gradient(180deg,
      var(--night) 0%, #0a0206 30%, #5a0006 48%, #c00000 62%, #d80000 82%, #a80000 100%);
  }
  .back-title {
    position: absolute;
    left: 0; right: 0;
    top: 36px;
    text-align: center;
    font-family: "Bodoni Moda", serif;
    font-weight: 400;
    font-size: 39px;
    line-height: 1;
    color: var(--red);
  }
</style>
</head>
<body>
  <section class="card card-front" aria-label="Business card front">
    <div class="accent-band"></div>
    <h1 class="studio-name">RKV Design Studio</h1>
    <p class="person-name">Tom Brazenhall AIA</p>
    <p class="person-role">Architecture Planning Interiors</p>

    <p class="contact-line contact-phone">
      <svg viewBox="0 0 18 18" aria-hidden="true"><rect x="5" y="0.5" width="9" height="17" rx="1.2"/><line x1="5" y1="2.5" x2="14" y2="2.5"/><line x1="5" y1="15.5" x2="14" y2="15.5"/></svg>
      614-529-4086
    </p>
    <p class="contact-line contact-email">
      <svg viewBox="0 0 18 18" aria-hidden="true"><rect x="0.5" y="3.5" width="17" height="11"/><polyline points="0.5,3.5 9,10 17.5,3.5"/></svg>
      rkvplanner4@mailvane.net
    </p>
    <p class="contact-line contact-web">
      <svg viewBox="0 0 18 18" aria-hidden="true"><circle cx="9" cy="9" r="8.3"/><ellipse cx="9" cy="9" rx="3.8" ry="8.3"/><line x1="0.7" y1="9" x2="17.3" y2="9"/><line x1="2" y1="5" x2="16" y2="5"/><line x1="2" y1="13" x2="16" y2="13"/></svg>
      www.rkvdesignstudio.net
    </p>
    <p class="contact-line contact-address">
      <svg viewBox="0 0 18 24" aria-hidden="true"><path d="M9 23.3 C4 16 1 12 1 8.5 A8 8 0 0 1 17 8.5 C17 12 14 16 9 23.3 Z"/><circle cx="9" cy="8.3" r="3"/></svg>
      418 Larkmoor Ave. #112 Columbus, Ohio 43215
    </p>
  </section>

  <section class="card card-back" aria-label="Business card back">
    <div class="building-photo" role="img" aria-label="Red-toned photograph of a modern glass campus building at dusk"></div>
    <h2 class="back-title">RKV Design Studio</h2>
  </section>
</body>
</html>
```